Business Card Design for company

We want new business cards. We'd like something different-- yet still highly professional. Our tagline is Providing leadership, delivering success. Stock photos are ok, as long as they are relevant and look upscale.

Target Market(s)

Architecture/Business Management Consulting/Engineering Consulting

Contact Information for Business Card

dark gray background with pops of blue might be good, but you tell me. You're the designers. Rounded corners might be nice, but again, you tell me.

Font styles to use
Serif
Sans Serif

Colors
3276b5
5c5c5c
9d9d9d
fbfbfb

Requirements
Nice to have
• Something different, but still very professional.

```html
<!DOCTYPE html>
<html lang="en">
<head>
<meta charset="utf-8">
<title>Corvex Group – Business Card</title>
<link rel="stylesheet" href="https://fonts.googleapis.com/css2?family=Montserrat:wght@400;500;600&display=swap">
<style>
  :root {
    --blue: #3276b5;
    --dark: #5c5c5c;
    --mid: #9d9d9d;
    --white: #fbfbfb;
    --stage: #e4e4e4;
    --ink: #3e3e3e;
  }
  * { margin: 0; padding: 0; box-sizing: border-box; }
  html, body {
    width: 1200px; height: 835px; overflow: hidden;
    background: var(--stage);
    font-family: "Montserrat", Arial, sans-serif;
  }
  .sheet {
    width: 1200px; height: 835px;
    display: flex; align-items: center; justify-content: center; gap: 40px;
  }
  .card {
    position: relative;
    width: 540px; height: 309px;
    border-radius: 10px; overflow: hidden;
    box-shadow: 0 6px 18px rgba(0,0,0,.18);
  }
  .card-shapes { position: absolute; inset: 0; width: 100%; height: 100%; display: block; }

  .wordmark {
    font-weight: 600; line-height: 1; letter-spacing: 1px;
    text-transform: uppercase; white-space: nowrap;
  }

  /* Front */
  .front .brand { position: absolute; right: 40px; bottom: 40px; }
  .front .wordmark { color: var(--blue); font-size: 32px; }
  .tagline {
    margin-top: 10px; font-size: 14px; font-weight: 500; line-height: 1.3;
    color: var(--dark);
  }

  /* Back */
  .back .brand { position: absolute; left: 270px; top: 64px; }
  .back .wordmark { color: var(--white); font-size: 26px; }
  .back .identity { position: absolute; left: 300px; top: 214px; color: var(--white); }
  .identity .name { font-size: 20px; font-weight: 500; letter-spacing: 1.5px; text-transform: uppercase; }
  .identity .role { font-size: 13px; margin-top: 3px; }

  .contact { position: absolute; left: 22px; top: 28px; color: var(--white); }
  .contact .name { font-size: 17px; font-weight: 600; letter-spacing: 1px; text-transform: uppercase; }
  .contact .role { font-size: 11px; color: var(--ink); margin-top: 2px; }
  .contact .address { font-size: 11px; color: var(--ink); margin-top: 10px; line-height: 1.4; }
  .contact-list { list-style: none; margin-top: 12px; }
  .contact-list li {
    display: flex; align-items: center; gap: 8px;
    font-size: 11.5px; line-height: 1.9; color: var(--white);
  }
  .contact-list svg { width: 13px; height: 13px; flex: none; fill: var(--white); }
</style>
</head>
<body>
<main class="sheet">

  <section class="card front" aria-label="Card front">
    <svg class="card-shapes" viewBox="0 0 540 309" preserveAspectRatio="none">
      <rect width="540" height="309" fill="var(--blue)"/>
      <path d="M300 0 C268 60 300 118 540 132 L540 0 Z" fill="var(--dark)"/>
      <path d="M300 0 C268 60 300 118 540 132" fill="none" stroke="var(--white)" stroke-width="5"/>
      <path d="M0 118 C180 142 380 150 540 178 L540 309 L0 309 Z" fill="var(--mid)"/>
      <path d="M0 118 C180 142 380 150 540 178" fill="none" stroke="var(--white)" stroke-width="6"/>
    </svg>
    <div class="brand">
      <div class="wordmark">Corvex Group</div>
      <p class="tagline">Guiding Strategy<br>Building Results</p>
    </div>
  </section>

  <section class="card back" aria-label="Card back">
    <svg class="card-shapes" viewBox="0 0 540 309" preserveAspectRatio="none">
      <rect width="540" height="309" fill="var(--dark)"/>
      <path d="M240 182 C330 178 440 164 540 146 L540 309 L256 309 C252 260 248 220 240 182 Z" fill="var(--blue)"/>
      <path d="M240 182 C330 178 440 164 540 146" fill="none" stroke="var(--white)" stroke-width="5"/>
      <path d="M0 0 L180 0 C220 90 246 210 256 309 L0 309 Z" fill="var(--mid)"/>
      <path d="M180 0 C220 90 246 210 256 309" fill="none" stroke="var(--white)" stroke-width="7"/>
    </svg>

    <div class="contact">
      <p class="name">Alan Mercer</p>
      <p class="role">CEO | Founder</p>
      <p class="address">480 Harbor Road,<br>Suite 210 Easton, NY 10020</p>
      <ul class="contact-list">
        <li><svg viewBox="0 0 24 24" aria-hidden="true"><path d="M6.6 10.8a15.2 15.2 0 0 0 6.6 6.6l2.2-2.2c.3-.3.7-.4 1-.2 1.1.4 2.3.6 3.6.6.6 0 1 .4 1 1V20c0 .6-.4 1-1 1A17 17 0 0 1 3 4c0-.6.4-1 1-1h3.5c.6 0 1 .4 1 1 0 1.3.2 2.5.6 3.6.1.3 0 .7-.2 1z"/></svg>555-014-2024</li>
        <li><svg viewBox="0 0 24 24" aria-hidden="true"><path d="M7 2h10v6H7zM4 9h16a2 2 0 0 1 2 2v7h-4v4H6v-4H2v-7a2 2 0 0 1 2-2zm4 8v3h8v-3z"/></svg>555-014-2023</li>
        <li><svg viewBox="0 0 24 24" aria-hidden="true"><path d="M2 5h20v14H2zm2 2v.5l8 5 8-5V7zm0 2.8V17h16V9.8l-8 5z"/></svg>mercer@corvexgroup.com</li>
        <li><svg viewBox="0 0 24 24" aria-hidden="true"><path d="M12 2a10 10 0 1 0 0 20 10 10 0 0 0 0-20zm6.9 6h-3a15 15 0 0 0-1.3-3.9A8 8 0 0 1 18.9 8zM12 4c.8 1.1 1.5 2.5 1.9 4h-3.8c.4-1.5 1.1-2.9 1.9-4zM4.3 14a8 8 0 0 1 0-4h3.4a16 16 0 0 0 0 4zm.8 2h3c.3 1.4.8 2.7 1.3 3.9A8 8 0 0 1 5.1 16zm3-8h-3a8 8 0 0 1 4.3-3.9C8.9 5.3 8.4 6.6 8.1 8zM12 20c-.8-1.1-1.5-2.5-1.9-4h3.8c-.4 1.5-1.100 2.9-1.9 4zm2.3-6H9.7a14 14 0 0 1 0-4h4.6a14 14 0 0 1 0 4zm.3 5.9c.5-1.2 1-2.5 1.3-3.9h3a8 8 0 0 1-4.3 3.9zm1.7-5.9a16 16 0 0 0 0-4h3.4a8 8 0 0 1 0 4z"/></svg>www.corvexgroup.com</li>
      </ul>
    </div>

    <div class="brand">
      <div class="wordmark">Corvex Group</div>
    </div>

    <div class="identity">
      <p class="name">Alan Mercer</p>
      <p class="role">CEO | Founder</p>
    </div>
  </section>

</main>
</body>
</html>
```